Following list to be designed:

1. A4 Letter Head

Must comprise of:
BRISK HARBOR and its LOGO
Address: No.41, 2F, Telvin Court, Marlow Lane, Upper Fennel Gardens, Bangalore 560 078
Tel: 080 41927380
Fax: 080 41927381
Mail: hello@briskharbor.example

Color of wordings to be in the lighter shade of blue and brighter shade of blue.

2. A4 Envelope

Must comprise of:
BRISK HARBOR and its LOGO
Tel: 080 41927380
Fax: 080 41927381

3. Postal Envelope

Must comprise of:
BRISK HARBOR and its LOGO
Tel: 080 41927380
Fax: 080 41927381

4. Business Card

Must comprise of:
Ravi Menon
Managing Partner
Cell: +91 9847162053
Mail: ravimenon@briskharbor.example
Tel: 080 41927380
Fax: 080 41927381

5. A4 Letter Head

Must comprise of:
BRISK HARBOR CORP. (wording) and BRISK HARBOR LOGO (only blue ribbon)

Blue ribbon (BRISK HARBOR LOGO) may be placed on Left Top Corner of the A4 Letter Head
and BRISK HARBOR CORP. (wording) to be placed on Right Top Corner of the A4 Letter Head

Tel: 080 41927380
Fax: 080 41927381

6. . A4 Envelope

Must comprise of:

Blue ribbon (BRISK HARBOR LOGO) may be placed on Left Top Corner of the A4 Envelope
and BRISK HARBOR CORP. (wording) to be placed on Right Top Corner of the A4 Envelope
Tel: 080 41927380
Fax: 080 41927381

Target Market(s)

Top IT/ITES Organizations

Industry/Entity Type

Real Estate Development

Font styles to use
Serif
Sans Serif

Colors
33a6d7
0792cd
85cae6

Requirements
Should not have
• Playful font and color

```html
<!DOCTYPE html>
<html lang="en">
<head>
<meta charset="utf-8">
<title>Brisk Harbor – Envelope</title>
<link rel="stylesheet" href="https://fonts.googleapis.com/css2?family=Noto+Sans:wght@400;600&display=swap">
<style>
  :root {
    --paper: #ffffff;
    --brand-blue: #0792cd;
    --brand-light: #33a6d7;
    --brand-grey: #6b6b66;
  }
  html, body {
    margin: 0;
    padding: 0;
    overflow: hidden;
    background: var(--paper);
  }
  .envelope {
    position: relative;
    width: 1200px;
    height: 551px;
    background: var(--paper);
    overflow: hidden;
    font-family: "Noto Sans", sans-serif;
  }
  .brand {
    position: absolute;
    left: 50px;
    top: 50px;
    display: flex;
    flex-direction: column;
    align-items: flex-start;
  }
  .brand-mark {
    width: 56px;
    height: 56px;
    margin-left: 58px;
    background: var(--brand-light);
  }
  .brand-name {
    margin: 14px 0 0;
    font-size: 21px;
    font-weight: 600;
    letter-spacing: 0.5px;
    color: var(--brand-grey);
    line-height: 1;
  }
  .sender {
    position: absolute;
    left: 49px;
    top: 366px;
    margin: 0;
    font-style: normal;
    font-size: 20.5px;
    line-height: 27.3px;
    color: var(--brand-blue);
    letter-spacing: 0.2px;
  }
  .sender span { display: block; }
</style>
</head>
<body>
  <main class="envelope">
    <header class="brand">
      <div class="brand-mark" aria-hidden="true"></div>
      <p class="brand-name">BRISK HARBOR</p>
    </header>
    <address class="sender">
      <span>No.41, 2F, Telvin Court, Marlow Lane</span>
      <span>Upper Fennel Gardens, Bangalore 560 078</span>
      <span>Tel: 080 41927380</span>
      <span>Fax: 080 41927381</span>
      <span>Mail: hello@briskharbor.example</span>
    </address>
  </main>
</body>
</html>
```